Software company stationery project
VOLTA Systems business cards, letterhead, stationery
Software company stationery project -
Creative Brief
Professional
Marcus Hale
President
217 Orchard Lane Tuckahoe, NY 10725
(855) 294-KOVU (5688)
marcus.hale@KovuSystems.example
www.kovusystems.example
Open to 2 sided or 1, and to your recommended font. Current website is under total reconstruction but the content will be similar. Would like to see if phrase could be used on card - "evidence and property specialists". Software is for police dept's. evidence/property rooms, and tracking those items.

```html
<!DOCTYPE html>
<html lang="en">
<head>
<meta charset="utf-8">
<title>VOLTA Systems Stationery</title>
<link rel="stylesheet" href="https://fonts.googleapis.com/css2?family=Roboto:wght@400;700;900&display=swap">
<style>
  :root {
    --backdrop: #d9d6d2;
    --paper: #ffffff;
    --paper-shade: #e4e4e4;
    --ink: #2b2b2b;
    --ink-soft: #555555;
    --band: #231f20;
    --band-light: #3c3a3a;
    --accent: #d2232a;
    --card-dark: #1d1d1d;
    --card-mid: #6a6a6a;
  }
  * { box-sizing: border-box; margin: 0; padding: 0; }
  html, body { width: 1200px; height: 761px; overflow: hidden; }
  body {
    background: var(--backdrop);
    font-family: "Roboto", Arial, sans-serif;
    color: var(--ink);
    position: relative;
  }
  .piece { position: absolute; overflow: hidden; box-shadow: 0 2px 6px rgba(0,0,0,.25); }
  .piece svg.bg { position: absolute; inset: 0; width: 100%; height: 100%; }

  .wordmark {
    font-weight: 900;
    color: var(--ink);
    line-height: 1;
    letter-spacing: .3px;
    display: flex;
    align-items: center;
    gap: 5px;
    white-space: nowrap;
  }
  .wordmark .dot { width: 7px; height: 7px; background: var(--accent); flex: none; }

  .contact { position: absolute; font-size: 6.5px; line-height: 1.45; color: var(--ink-soft); white-space: nowrap; }
  .contact b { color: var(--ink); font-weight: 700; }

  /* Business card */
  .business-card { left: 29px; top: 132px; width: 180px; height: 108px; background: linear-gradient(135deg, var(--card-mid), var(--card-dark) 70%); }
  .business-card .wordmark { position: absolute; left: 12px; top: 40px; font-size: 12px; color: #f2f2f2; }
  .business-card .holder { position: absolute; right: 12px; top: 12px; text-align: right; color: #f2f2f2; font-size: 7px; font-weight: 700; }
  .business-card .holder span { display: block; font-size: 5px; font-weight: 400; color: #cfcfcf; }
  .business-card .contact { left: 12px; top: 64px; font-size: 5px; color: #d6d6d6; }
  .business-card .contact b { color: #ffffff; }

  /* Letterhead */
  .letterhead { left: 233px; top: 96px; width: 456px; height: 643px; background: linear-gradient(160deg, var(--paper) 40%, var(--paper-shade)); }
  .letterhead .wordmark { position: absolute; left: 60px; top: 30px; font-size: 12px; }
  .letterhead .contact.header { left: 170px; top: 20px; }
  .letterhead .contact.footer { left: 84px; top: 520px; }

  /* Envelope back */
  .envelope-back { left: 694px; top: 96px; width: 482px; height: 283px; background: linear-gradient(160deg, var(--paper) 40%, var(--paper-shade)); }
  .envelope-back .wordmark { position: absolute; left: 48px; top: 86px; font-size: 12px; }
  .envelope-back .wordmark.flap { left: 245px; top: 14px; font-size: 10px; transform: rotate(180deg); }
  .envelope-back .contact { left: 180px; top: 76px; }

  /* Envelope front */
  .envelope-front { left: 694px; top: 396px; width: 482px; height: 276px; background: linear-gradient(180deg, var(--paper-shade), var(--paper) 35%); }
  .envelope-front .wordmark { position: absolute; left: 50%; top: 56px; transform: translateX(-50%); font-size: 13px; }
</style>
</head>
<body>

<section class="piece business-card" aria-label="Business card">
  <div class="holder">Marcus Hale<span>President</span></div>
  <div class="wordmark"><span class="dot"></span>VOLTA Systems</div>
  <div class="contact">
    <b>Address:</b> 217 Orchard Lane Tuckahoe, NY 10725<br>
    <b>Toll free:</b> (855) 294-KOVU (5688)<br>
    <b>Email:</b> marcus.hale@KovuSystems.example<br>
    <b>Web:</b> www.kovusystems.example
  </div>
</section>

<section class="piece letterhead" aria-label="Letterhead">
  <svg class="bg" viewBox="0 0 456 643" preserveAspectRatio="none" aria-hidden="true">
    <path d="M0 0 H42 C38 200 92 430 50 643 H0 Z" fill="var(--band)"/>
    <path d="M42 0 C38 200 92 430 50 643 H55 C97 430 44 200 47 0 Z" fill="var(--accent)"/>
    <path d="M47 0 C44 200 97 430 55 643 H60 C102 430 50 200 52 0 Z" fill="var(--band-light)" opacity=".35"/>
  </svg>
  <div class="wordmark"><span class="dot"></span>VOLTA Systems</div>
  <div class="contact header">
    <b>Address:</b> 217 Orchard Lane Tuckahoe, NY 10725<br>
    <b>Toll free:</b> (855) 294-KOVU (5688)<br>
    <b>Cell:</b> (914) 555-0142 <b>Fax:</b> (914) 555-0178<br>
    <b>Email:</b> marcus.hale@KovuSystems.example<br>
    <b>Web:</b> www.kovusystems.example
  </div>
  <div class="contact footer">
    <b>Address:</b> 217 Orchard Lane Tuckahoe, NY 10725<br>
    <b>Toll free:</b> (855) 294-KOVU (5688)<br>
    <b>Cell:</b> (914) 555-0142 <b>Fax:</b> (914) 555-0178<br>
    <b>Email:</b> marcus.hale@KovuSystems.example<br>
    <b>Web:</b> www.kovusystems.example
  </div>
</section>

<section class="piece envelope-back" aria-label="Envelope, address side">
  <svg class="bg" viewBox="0 0 482 283" preserveAspectRatio="none" aria-hidden="true">
    <path d="M0 0 H26 C22 90 48 180 30 283 H0 Z" fill="var(--band)"/>
    <path d="M26 0 C22 90 48 180 30 283 H34 C52 180 26 90 30 0 Z" fill="var(--accent)"/>
  </svg>
  <div class="wordmark flap">VOLTA Systems</div>
  <div class="wordmark"><span class="dot"></span>VOLTA Systems</div>
  <div class="contact">
    <b>Address:</b> 217 Orchard Lane Tuckahoe, NY 10725<br>
    <b>Toll free:</b> (855) 294-KOVU (5688)<br>
    <b>Cell:</b> (914) 555-0142 <b>Fax:</b> (914) 555-0178<br>
    <b>Email:</b> marcus.hale@KovuSystems.example<br>
    <b>Web:</b> www.kovusystems.example
  </div>
</section>

<section class="piece envelope-front" aria-label="Envelope, flap side">
  <svg class="bg" viewBox="0 0 482 276" preserveAspectRatio="none" aria-hidden="true">
    <path d="M0 0 L241 118 L482 0" fill="none" stroke="#cfcfcf" stroke-width="1"/>
  </svg>
  <div class="wordmark"><span class="dot"></span>VOLTA Systems</div>
</section>

</body>
</html>
```